Website Design for Kids

We need to redesign our site pumblewok.net.
Current site was done long ago in Flash. We need to remove Flash and create a responsive site which can be viewed on phone, tablets as well as PC.
We are looking for a new fresh design. No elements from existing design need to be incorporated into new design.
The site is targeted for kids 7-12 years old.
Design should have attractive colors and it should be easy to navigate. It will be even better to provide one theme for boys and one for girls.
New site will have following features:
SHORT STORIES
Ability to display thumbnails of stories available. When user click a story it will play.
See http://pumblewok.net/stories/index.asp to get an idea.
MOVIES
We have two moves, more to come. Users will be able to see thumbnails and watch trailers. To watch full movie they will be redirect to a Plorvu page where they can pay and watch.
See http://pumblewok.net/Movies/ to get an idea.
PICTURE STORIES
This will feature short stories. When a story is clicked it will start playing. The stories will have picture and text, possibly audio too.
See http://pumblewok.net/stories/stories.asp to get an idea.
AUDIO STORIES
Audio stories recorded from kids or adults will be played. Optional photo of the person who recorded story will be displayed. User will have option to select a story by clicking thumbnail of stories.
VIDEO STORIES
Like audio stories, user will be able to scroll though thumbnails of stories and play one. Short video 1-3 mins will be played.
- I have upgraded budget and added a few more simple requirements. Need to decide soon so please submit your designs asap.
Number of Pages Required
5+ page

```html
<!DOCTYPE html>
<html lang="en">
<head>
<meta charset="utf-8">
<title>Pumblewok – Stories, Movies and Fun for Kids</title>
<link rel="stylesheet" href="https://fonts.googleapis.com/css2?family=Bubblegum+Sans&family=Roboto:wght@400;500&family=Open+Sans:ital,wght@1,600&display=swap">
<style>
:root{
  --sky:#bfe3f7;
  --sky-deep:#9fd2f0;
  --teal:#1aa8b4;
  --teal-dark:#147d87;
  --teal-frame:#1b9fa8;
  --red:#d9182a;
  --blue:#2aa6d9;
  --yellow:#f2b51c;
  --magenta:#a0116e;
  --green:#5aa51f;
  --orange:#f26a10;
  --black:#1e1e1e;
  --crimson:#d10f3c;
  --purple:#5a2a9c;
  --text:#444;
  --white:#fff;
  --card:#f8f8f8;
}
*{margin:0;padding:0;box-sizing:border-box}
html,body{width:999px;height:1200px;overflow:hidden}
body{
  position:relative;
  font-family:"Roboto",Arial,sans-serif;
  color:var(--text);
  background:radial-gradient(ellipse at 50% 45%,#d8effb 0%,var(--sky) 55%,var(--sky-deep) 100%);
}
.abs{position:absolute}
.display{font-family:"Bubblegum Sans",cursive;font-weight:400;white-space:nowrap}

/* header */
.search-btn{left:143px;top:42px;width:48px;height:48px;border-radius:50%;background:var(--teal);border:2px solid #dff;box-shadow:0 2px 4px rgba(0,0,0,.2)}
.search-btn svg{display:block}
.search-field{left:188px;top:48px;width:139px;height:37px;border-radius:4px;background:linear-gradient(#f4f4f4,#e4e4e4);border:1px solid #ccc}
.brand{left:432px;top:36px;width:150px;display:flex;align-items:center;gap:6px;font-size:32px;color:var(--purple)}
.brand-dot{width:14px;height:14px;border-radius:50%;background:var(--purple)}
.social{left:733px;top:53px;display:flex;gap:7px}
.social span{width:26px;height:26px;border-radius:50%;box-shadow:0 2px 3px rgba(0,0,0,.25)}
.social .s1{background:#29a9e0}.social .s2{background:#2c4f9b}.social .s3{background:#444}.social .s4{background:#e0457b}

/* nav */
.main-nav{left:143px;top:131px;width:714px;height:37px;display:flex}
.main-nav a{flex:1;display:flex;align-items:center;justify-content:center;color:var(--white);text-decoration:none;font-size:14px;text-transform:uppercase;white-space:nowrap}
.n1{background:var(--red)}.n2{background:var(--blue)}.n3{background:var(--yellow)}.n4{background:var(--magenta)}.n5{background:var(--green)}.n6{background:var(--orange)}.n7{background:var(--black)}

/* slider */
.hero{left:143px;top:168px;width:714px;height:351px;border:6px solid var(--teal-frame);border-bottom-width:7px;box-shadow:0 8px 10px -6px rgba(0,0,0,.25);overflow:hidden}
.hero-art{position:absolute;inset:0;background:linear-gradient(100deg,#f7c94a 0%,#f5b93a 45%,#f2a73a 70%,#e9b04a 100%)}
.hero-caption{left:56px;top:117px;width:311px;height:103px;background:rgba(255,255,255,.72);padding:20px 28px}
.hero-caption h1{font-size:25px;color:var(--crimson);line-height:1}
.hero-caption p{font-size:10px;line-height:18px;margin-top:8px;color:#555}
.arrow{top:147px;width:36px;height:40px;background:rgba(255,255,255,.65);display:flex;align-items:center;justify-content:center}
.arrow.prev{left:1px}.arrow.next{right:1px}

/* feature cards */
.card{top:547px;width:230px;height:287px;background:var(--card);box-shadow:0 3px 4px rgba(0,0,0,.12)}
.card-head{height:39px;display:flex;align-items:center;justify-content:center;font-size:15px;color:var(--white);position:relative}
.card-head::after{content:"";position:absolute;inset:5px 7px 0;border:1px dashed rgba(255,255,255,.55);border-bottom:none}
.card-art{height:127px}
.card p{font-size:8px;line-height:16px;padding:11px 10px 0;text-align:justify}
.more{margin:16px auto 0;width:64px;height:24px;border-radius:12px;color:var(--white);font-size:8px;font-style:italic;font-weight:500;display:flex;align-items:center;justify-content:center;border:2px solid rgba(255,255,255,.7);box-shadow:0 0 0 1px rgba(0,0,0,.1)}
.c-stories{left:143px}.c-stories .card-head,.c-stories .more{background:var(--green)}
.c-movies{left:386px}.c-movies .card-head,.c-movies .more{background:var(--teal)}
.c-pictures{left:628px}.c-pictures .card-head,.c-pictures .more{background:var(--crimson)}

/* lower panel */
.lower{left:143px;top:854px;width:714px;height:215px;background:var(--teal);border-radius:2px;box-shadow:0 8px 10px -6px rgba(0,0,0,.3)}
.slideshow{left:23px;top:22px;width:160px;height:170px;background:#333;border-radius:2px;overflow:hidden}
.slideshow h2{height:29px;background:var(--orange);color:var(--white);font-size:15px;display:flex;align-items:center;justify-content:center}
.slideshow .art{height:117px;background:linear-gradient(160deg,#2b3b5e,#5f6f8f 60%,#9aa3b5)}
.slideshow figcaption{height:24px;color:var(--white);font-size:9px;display:flex;align-items:center;justify-content:center}
.quick{left:213px;top:20px;width:276px;height:172px;background:var(--teal-dark);border-radius:3px}
.quick .art{position:absolute;left:14px;top:18px;width:123px;height:141px;background:linear-gradient(180deg,#e58a1e 0%,#b05a14 60%,#3b2a8a 62%,#5c2ec5 100%);border:1px solid #fff}
.quick h3{position:absolute;left:146px;top:19px;font-size:11px;line-height:13px;color:var(--white);transform:scaleX(.88);transform-origin:left center}
.quick ul{position:absolute;left:146px;top:39px;list-style:none}
.quick li{font-size:10px;color:var(--white);height:21.5px;display:flex;align-items:center;gap:9px;white-space:nowrap}
.quick li::before{content:"";width:7px;height:7px;border-radius:50%;background:var(--orange)}
.share{left:514px;top:24px;width:190px;color:var(--white);font-size:12px;line-height:15px}
.share-form{left:514px;top:67px;display:flex}
.share-form .field{width:117px;height:22px;background:var(--white);font-size:8px;color:#666;padding:6px 7px}
.share-form .send{width:53px;height:22px;background:var(--red);color:var(--white);font-size:10px;display:flex;align-items:center;justify-content:center}
.updates{left:511px;top:114px;width:172px;height:75px;background:var(--green);border-radius:2px;padding:12px 14px}
.updates h4{font-size:10px;line-height:12px;color:var(--white);text-align:center;transform:scaleX(.92)}
.updates .row{display:flex;margin-top:12px;justify-content:center}
.updates .field{width:121px;height:21px;background:var(--white);border-radius:3px 0 0 3px}
.updates .go{width:22px;height:21px;background:var(--orange);color:var(--white);font-size:8px;display:flex;align-items:center;justify-content:center;border-radius:0 3px 3px 0}

/* footer */
.site-foot{left:222px;top:1088px;width:554px;height:92px;border:1px dashed rgba(255,255,255,.7);text-align:center}
.foot-links{margin-top:14px;font-size:9px;color:#222}
.foot-links a{color:#222;text-decoration:none}
.foot-info,.foot-copy{font-family:"Open Sans",Arial,sans-serif;font-style:italic;font-weight:600;font-size:11px;color:#666;margin-top:9px;white-space:nowrap}
</style>
</head>
<body>

<header>
  <div class="abs search-btn">
    <svg width="44" height="44" viewBox="0 0 44 44"><circle cx="20" cy="20" r="8" fill="none" stroke="#fff" stroke-width="2"/><line x1="26" y1="26" x2="32" y2="32" stroke="#fff" stroke-width="3" stroke-linecap="round"/><line x1="16" y1="20" x2="24" y2="20" stroke="#fff" stroke-width="2"/><line x1="20" y1="16" x2="20" y2="24" stroke="#fff" stroke-width="2"/></svg>
  </div>
  <div class="abs search-field"></div>
  <div class="abs brand display"><span class="brand-dot"></span>Pumblewok</div>
  <div class="abs social" aria-label="Social links"><span class="s1"></span><span class="s2"></span><span class="s3"></span><span class="s4"></span></div>
</header>

<nav class="abs main-nav">
  <a class="n1" href="#">Home</a><a class="n2" href="#">Game</a><a class="n3" href="#">Stories</a><a class="n4" href="#">Movies</a><a class="n5" href="#">Activities</a><a class="n6" href="#">Fun Stuff</a><a class="n7" href="#">Shop</a>
</nav>

<section class="abs hero">
  <div class="hero-art" role="img" aria-label="Cartoon boy sitting on a wooden bench in a sunny yellow room with an autumn painting"></div>
  <div class="abs hero-caption">
    <h1 class="display">PUMBLEWOK</h1>
    <p>Lorem Ipsum has been the industry's standard dummy text ever since the 1500s, when an unknown printer</p>
  </div>
  <div class="abs arrow prev"><svg width="14" height="18" viewBox="0 0 14 18"><path d="M10 2 L3 9 L10 16" fill="none" stroke="#333" stroke-width="3"/></svg></div>
  <div class="abs arrow next"><svg width="14" height="18" viewBox="0 0 14 18"><path d="M4 2 L11 9 L4 16" fill="none" stroke="#333" stroke-width="3"/></svg></div>
</section>

<article class="abs card c-stories">
  <div class="card-head display">SHORT STORIES</div>
  <div class="card-art" role="img" aria-label="Illustrated story scene with travellers and a cart among palm trees" style="background:linear-gradient(180deg,#9fd0e8 0%,#b7d98a 45%,#6fae3a 100%)"></div>
  <p>Lorem Ipsum has been the industry's standard dummy text ever since the 1500s, when an unknown printer took a galley of type and scrambled it to make a type specimen book. It has survived not only five centuries</p>
  <span class="more">Read More</span>
</article>

<article class="abs card c-movies">
  <div class="card-head display">MOVIES</div>
  <div class="card-art" role="img" aria-label="Movie poster with a scroll title under a starry night sky" style="background:linear-gradient(180deg,#4a1fa8 0%,#6d2fd6 60%,#3a2a5a 100%)"></div>
  <p>Lorem Ipsum has been the industry's standard dummy text ever since the 1500s, when an unknown printer took a galley of type and scrambled it to make a type specimen book. It has survived not only five centuries</p>
  <span class="more">Read More</span>
</article>

<article class="abs card c-pictures">
  <div class="card-head display">PICTURE STORIES</div>
  <div class="card-art" role="img" aria-label="Picture story scene with figures and scales among clouds" style="background:radial-gradient(circle at 55% 50%,#ffffff 0%,#dcefff 45%,#9cc9ea 100%)"></div>
  <p>Lorem Ipsum has been the industry's standard dummy text ever since the 1500s, when an unknown printer took a galley of type and scrambled it to make a type specimen book. It has survived not only five centuries</p>
  <span class="more">Read More</span>
</article>

<section class="abs lower">
  <figure class="abs slideshow">
    <h2 class="display">SLIDE SHOW</h2>
    <div class="art" role="img" aria-label="Slide show picture of a winged horse under a crescent moon"></div>
    <figcaption>INDONESIA</figcaption>
  </figure>

  <div class="abs quick">
    <div class="art" role="img" aria-label="Movie thumbnails with a sunset scene and a starry night"></div>
    <h3 class="display">VISIT THESE QUICK LINKS</h3>
    <ul>
      <li>Play Puzzle Fun</li><li>Send An E-card</li><li>Watch the Ark</li><li>Click N Color</li><li>Word Search</li><li>Click On Game</li>
    </ul>
  </div>

  <p class="abs share">Send this page to a friend,<br>Enter email here</p>
  <div class="abs share-form"><span class="field">Eamil</span><span class="send">SEND</span></div>

  <div class="abs updates">
    <h4 class="display">ADD YOUR E-MAIL FOR UPDATES</h4>
    <div class="row"><span class="field"></span><span class="go">GO</span></div>
  </div>
</section>

<footer class="abs site-foot">
  <div class="foot-links"><a href="#">Home</a> &nbsp;|&nbsp; <a href="#">Game</a> &nbsp;|&nbsp; <a href="#">Stories</a> &nbsp;|&nbsp; <a href="#">Movies</a> &nbsp;|&nbsp; <a href="#">Activities</a> &nbsp;|&nbsp; <a href="#">Fun stuff</a> &nbsp;|&nbsp; <a href="#">Shop</a></div>
  <p class="foot-info">Fernvale, USA| Tel -555 014 2290| Email - info@pumblewok.net</p>
  <p class="foot-copy">Copyright© 2009 - 2015 All Rights.</p>
</footer>

</body>
</html>
```